BRIGHTWATER BUILDERS, INC. ELECTRICAL SERVICE

We need a tri-fold pamphlet design for electrical service based in NW Arkansas. We offer Commercial and Industrial Electrical Services including: Infrared imaging, Data Cable Testing, Fiber Optics Testing & Repair, Utility Locates, Preventative Maintenance, Lighting Inspections, Electrical Equipment Cleaning, Automatic Transfer Switch Testing, LED Upgrades with Energy Savings Report.

```html
<!DOCTYPE html>
<html lang="en">
<head>
<meta charset="utf-8">
<title>Brightwater Builders – Electrical Service Tri-fold</title>
<link href="https://fonts.googleapis.com/css2?family=Open+Sans:wght@400;600;700&family=Libre+Baskerville:wght@400;700&family=Oswald:wght@400&display=swap" rel="stylesheet">
<style>
:root{
  --kraft:#a87b53;
  --blue:#2a4fa8;
  --blue-dark:#1f3f91;
  --blue-light:#8fb5e6;
  --grey:#dcdcdc;
  --panel-grey:#e6e6e8;
  --text:#333;
  --white:#fff;
}
*{box-sizing:border-box;margin:0;padding:0}
html,body{width:867px;height:1200px;overflow:hidden}
body{background:var(--kraft);font-family:"Open Sans",Arial,sans-serif;color:var(--text);position:relative}
.side-label{position:absolute;left:0;width:867px;text-align:center;color:var(--white);font-weight:700;font-size:27px}
.sheet{position:absolute;left:101px;width:695px;height:491px;background:var(--white);box-shadow:0 10px 12px rgba(0,0,0,.35)}
.sheet-1{top:83px}
.sheet-2{top:612px}
.abs{position:absolute}
.band{position:absolute;left:0;right:0;bottom:0;height:14px;background:linear-gradient(90deg,var(--blue-dark),var(--blue-light) 45%,var(--blue-dark))}
.photo{position:absolute}
.hex{clip-path:polygon(25% 0,75% 0,100% 50%,75% 100%,25% 100%,0 50%)}
.hex-frame{background:var(--blue)}
.checklist{list-style:none}
.checklist li{position:relative;padding-left:13px}
.checklist li::before{content:"";position:absolute;left:0;top:2px;width:8px;height:8px;border-radius:50%;background:var(--blue)}
.checklist li::after{content:"";position:absolute;left:2.6px;top:3.5px;width:2px;height:3.5px;border:solid var(--white);border-width:0 1.2px 1.2px 0;transform:rotate(45deg)}
.checklist.on-blue li::before{background:var(--white)}
.checklist.on-blue li::after{border-color:var(--blue)}
.brand{display:flex;align-items:center;gap:6px;color:var(--blue);font-weight:700;line-height:1.05}
.brand-dot{width:16px;height:16px;border-radius:50%;background:var(--blue);flex:none}
.serif-head{font-family:"Libre Baskerville",Georgia,serif;color:var(--blue);font-weight:400;white-space:nowrap}
.web-bar{left:0;top:0;width:232px;height:35px;background:var(--grey);font-weight:700;font-size:13px;padding:13px 0 0 17px;color:#222;letter-spacing:.3px}
.services{left:0;top:35px;width:232px;height:456px;background:var(--blue)}
.services h2{position:absolute;left:17px;top:18px;color:var(--white);font-size:13.5px;font-weight:600;letter-spacing:.3px}
.services .checklist{position:absolute;left:17px;top:40px;color:var(--white);font-size:7.6px;line-height:14.9px;letter-spacing:.2px}
.about{left:18px;top:233px;width:199px;height:242px;background:var(--panel-grey);padding:10px 10px}
.about h3{text-align:center;font-size:14px;font-weight:600;letter-spacing:1px;color:#333}
.about p{font-family:"Libre Baskerville",Georgia,serif;font-size:6.4px;line-height:10.6px;text-align:justify;text-align-last:center;margin-top:7px}
.call-bar{left:232px;top:0;width:231px;height:35px;background:var(--blue);color:var(--white);font-size:14px;text-align:center;padding-top:9px}
.call-bar b{font-weight:700}
.center-col{left:232px;top:35px;width:231px;height:456px;background:linear-gradient(#fff,#f1f1f3)}
.center-col .brand{position:absolute;left:50px;top:22px;font-size:13px}
.center-col h2{position:absolute;left:0;width:231px;top:93px;text-align:center;font-size:13px}
.center-col .intro{position:absolute;left:14px;width:204px;top:115px;font-family:"Libre Baskerville",Georgia,serif;font-size:6.4px;line-height:10.7px;text-align:justify;text-align-last:center}
.address{left:247px;top:413px;width:201px;height:62px;background:var(--blue);color:var(--white);border-radius:3px;text-align:center;font-size:7.6px;line-height:12.6px;padding-top:5px}
.cover{left:463px;top:0;width:232px;height:491px;background:linear-gradient(135deg,#cfd6df 0%,#f4f5f7 35%,#fff 60%)}
.cover-titles{position:absolute;left:0;width:232px;top:233px;text-align:center}
.cover-titles .line1{font-size:14.4px;font-weight:700;line-height:18px;color:#222}
.cover-titles hr{border:0;border-top:1px solid #c8c8c8;margin:3px 17px}
.cover-titles .line2{font-size:19px;font-weight:700;color:var(--blue);letter-spacing:.5px;line-height:24px}
.cover-titles .line3{font-size:14.4px;font-weight:700;line-height:18px;color:#222;margin-top:6px}
.cover .brand{position:absolute;left:30px;top:400px;font-size:15px}
.col-a{left:0;top:0;width:232px;padding:0 10px 0 20px}
.col-a h2{font-size:11px;margin-top:25px}
.col-a p{font-size:7.5px;line-height:11.6px;text-align:justify;margin-top:12px}
.col-a p+p{margin-top:5px}
.col-a h2.second{font-size:11.4px;margin-top:22px}
.col-a .checklist{font-size:7.5px;line-height:10.8px;margin-top:9px}
.col-a .checklist li{margin-bottom:3.5px}
.other-work{left:21px;top:413px;width:198px;height:62px;background:var(--blue);border-radius:3px;display:flex;overflow:hidden}
.other-work .tag{background:#9a9a9a;width:46px;color:var(--white);font-family:"Oswald",sans-serif;font-size:14px;line-height:16.5px;text-align:center;padding-top:5px;flex:none}
.other-work .areas{color:var(--white);font-weight:700;font-style:italic;font-size:7.4px;line-height:11.8px;padding:5px 6px}
.col-b{left:232px;top:148px;width:231px;height:329px;background:#eeeff2;padding:8px 13px 0 13px}
.col-b h2{font-size:14.5px;letter-spacing:1px}
.col-b p{font-size:7.5px;line-height:11.6px;text-align:justify;margin-top:9px}
.col-b .checklist{font-size:7.5px;line-height:14px;margin-top:10px}
.col-b .closing{margin-top:6px;text-align:left}
.col-c{left:463px;top:0;width:232px;padding:0 10px 0 17px}
.col-c h2{font-size:12px;margin-top:25px}
.col-c .checklist{font-size:7.5px;line-height:10.2px;margin-top:8px}
.col-c .checklist li{margin-bottom:3.8px}
.dealer-box{left:477px;top:191px;width:198px;height:53px;background:var(--blue);color:var(--white);border-radius:3px;font-size:9.6px;font-weight:700;text-align:center;line-height:14px;padding-top:5px}
.genset-photo .brand{position:absolute;left:8px;bottom:14px;font-size:10px;background:rgba(255,255,255,.85);padding:4px 6px;border-radius:2px}
</style>
</head>
<body>

<div class="side-label" style="top:30px">Side 1</div>

<section class="sheet sheet-1">
  <div class="abs web-bar">www.brightwater-build.net</div>
  <div class="abs services">
    <h2>SERVICES INCLUDING</h2>
    <ul class="checklist on-blue">
      <li>INFRARED IMAGING,</li>
      <li>DATA CABLE TESTING,</li>
      <li>FIBER OPTICS TESTING &amp; REPAIR,</li>
      <li>UTILITY LOCATES,</li>
      <li>PREVENTATIVE MAINTENANCE,</li>
      <li>LIGHTING INSPECTIONS,</li>
      <li>ELECTRICAL EQUIPMENT CLEANING,</li>
      <li>AUTOMATIC TRANSFER SWITCH TESTING,</li>
      <li>LED UPGRADES WITH ENERGY SAVINGS REPORT</li>
    </ul>
  </div>
  <div class="abs about">
    <h3>ABOUT US</h3>
    <p>Since 1972, Brightwater has been serving Northwest Arkansas. As our customers needed more services, we expanded our workforce, our equipment, our technology, and our capacity to meet those needs. Today, we provide complete contracting and engineering services for clients across the nation and around the world.</p>
    <div class="photo" role="img" aria-label="Company awards and plaques displayed on a table" style="left:21px;top:117px;width:155px;height:116px;background:linear-gradient(135deg,#7a3b22,#b0603a 50%,#5a2a18)"></div>
  </div>

  <div class="abs call-bar">Call Us: <b>479.555.0142</b></div>
  <div class="abs center-col">
    <div class="brand"><span class="brand-dot"></span>BRIGHTWATER<br>BUILDERS, INC.</div>
    <h2 class="serif-head">From concept to completion</h2>
    <p class="intro">Brightwater's diversified workforce is comprised of over 600 expert craftspeople; with an offering of mechanical, electrical contracting and specialized services, we provide a 360-degree approach for comprehensive contracting solutions.</p>
  </div>
  <div class="abs hex hex-frame" style="left:241px;top:213px;width:212px;height:185px"></div>
  <div class="photo hex" role="img" aria-label="Bright industrial workshop with hanging cable reels and red workbenches" style="left:244px;top:216px;width:206px;height:179px;background:linear-gradient(180deg,#d8dade,#eceae4 55%,#b8553c 80%,#d6d3cc)"></div>
  <div class="abs address">
    1450 North Cedar Road, P.O. Box 420<br>
    Lakemont, MO 65999-0420<br>
    <b>Phone:</b> 479.555.0142<br>
    <b>Toll-Free:</b> 800.555.0199
  </div>

  <div class="abs cover">
    <div class="cover-titles">
      <div class="line1">RESIDENTIAL AND<br>COMMERCIAL/INDUSTRIAL</div>
      <hr>
      <div class="line2">ELECTRICAL SERVICE</div>
      <hr>
      <div class="line3">GENERATOR SALES<br>AND SERVICE</div>
    </div>
    <div class="brand"><span class="brand-dot"></span>BRIGHTWATER<br>BUILDERS, INC.</div>
  </div>
  <div class="abs hex hex-frame" style="left:474px;top:33px;width:200px;height:172px"></div>
  <div class="photo hex" role="img" aria-label="Electrician in hard hat holding a sparking power cable" style="left:477px;top:36px;width:194px;height:166px;background:radial-gradient(circle at 45% 25%,#e8f4ff,#4d86d9 35%,#12285e 85%)"></div>
  <div class="band"></div>
</section>

<section class="sheet sheet-2">
  <div class="abs col-a">
    <h2 class="serif-head">Division 88 Electrical Contractors</h2>
    <p>From design-build and project management services to complete new-construction services, implementation, and maintenance, Brightwater is ready to meet your needs in electrical engineering and contracting.</p>
    <p>BWB can provide full MEP services, or we can step in when you need specialized services.</p>
    <h2 class="serif-head second">24-Hour Service 7 Days a Week</h2>
    <ul class="checklist">
      <li>Complete commercial, industrial and institutional services</li>
      <li>Service and updating of electrical systems and substations</li>
      <li>Design-build capabilities with licensed engineers on staff</li>
      <li>Qualified personnel to service the industrial needs from repairs and retrofits to complete systems</li>
      <li>A staff of full-time estimators to ensure timely turnaround project quotes</li>
      <li>Installation, replacement and repair of poles, lighting and transformers</li>
      <li>Lineman, bucket truck, commercial pole setting equipment</li>
      <li>Thermography</li>
    </ul>
  </div>
  <div class="abs other-work">
    <div class="tag">OTHER<br>WORK<br>AREA</div>
    <div class="areas">HVAC, Generators, Automation + Robotics, Electrical, Mechanical/ Plumbing, Fabrication/Millwright, Cranes + Rigging, Sheet Metal</div>
  </div>

  <div class="photo" role="img" aria-label="Lineman in a bucket truck working on a utility pole" style="left:232px;top:0;width:118px;height:148px;background:linear-gradient(180deg,#4f86c6,#9cc2e6 60%,#6b7c86)"></div>
  <div class="photo" role="img" aria-label="Open electrical control panel with wiring and breakers" style="left:350px;top:0;width:113px;height:148px;background:linear-gradient(90deg,#3a3d42,#c9ccd0 35%,#e2e3e5 65%,#50545a)"></div>
  <div class="abs col-b">
    <h2 class="serif-head">GENERATORS</h2>
    <p>Emergency generators start and run automatically when you have a power outage. That means peace of mind, whether you're ensuring that your inventory maintains the required storage temperature or keeping your family comfortable.</p>
    <p>Brightwater Builders is now offering service for emergency or backup generators for residential and light commercial applications. You can come to us for sales, installation, and service of emergency generators for home or business.</p>
    <p>Choose Brightwater for the top brands of generators, including Voltex and Harlan. Then stick with us for installation and service in the years to come.</p>
    <ul class="checklist">
      <li>Service 24/7, 365 days a year</li>
      <li>Factory trained technicians</li>
      <li>Fully equipped service vehicles</li>
      <li>Complete inventory to handle all service calls</li>
      <li>Annual Preventative Maintenance contracts</li>
    </ul>
    <p class="closing">For a consultation for a whole home generator or one for your business, <b>contact us today at 479-555-0177</b></p>
  </div>

  <div class="abs col-c">
    <h2 class="serif-head">Telecommunications</h2>
    <ul class="checklist">
      <li>Certified Fiber Optic Technicians</li>
      <li>With Over 30 Years Combined Experienced</li>
      <li>Experienced Installating both Single-mode and Muli-mode</li>
      <li>Emergency Fusion and Mechanical Splicing</li>
      <li>Data Networks Installation and troubleshooting</li>
      <li>Access Control</li>
      <li>Modifications and improvements</li>
      <li>Control Systems</li>
    </ul>
  </div>
  <div class="abs dealer-box">Sales, Service, Repair, Installation, Trained In Voltex, Harlan, and Corwin.</div>
  <div class="photo genset-photo" role="img" aria-label="Workers beside a large outdoor switchgear and generator installation" style="left:463px;top:244px;width:232px;height:233px;background:linear-gradient(180deg,#d4d8de,#a9b0ba 45%,#8a8478 80%,#b9ad96)">
    <div class="brand"><span class="brand-dot" style="width:11px;height:11px"></span>BRIGHTWATER<br>BUILDERS, INC.</div>
  </div>
  <div class="band"></div>
</section>

<div class="side-label" style="top:1113px">Side 2</div>

</body>
</html>
```